Business Cards for our company

Hi there,

we have successfully designed a logo with ArtHive and would like now to design our business cards. We would like to keep the colours and the look-and-feel of the logo. Please send in variations with two or three colours and one or two sides. I promise to respond to every single submission.

Many thanks and happy new year.

All the best,
Gustav

Target Market(s)

B2B

Industry/Entity Type

Trade

Contact Information for Business Card

We have successfully designed a logo with ArtHive and would like now to design our business cards. We would like to keep the colours and the look-and-feel of the logo. Please send in variations with two or three colours and one or two sides. I promise to respond to every single submission.

Font styles to use
Serif
Sans Serif
Script

Requirements
Must have
• These information should be on the business card, grouped as you suggest, and we think using small pictograms for mobile, email, etc is pretty helpful:
• Gustav Ortlieb (first and second name)
• Geschäftsführer/ Managing Director (title)
• KtK Warenkontor GmbH (company name and legal form)
• Hasenbergsteige 31/2 (street and house number)
• 70912 Lindenbach (zip code and town)
• +491609381746 (mobile)
• +4971419273065 (work)
• g.ortlieb@ktk-warenkontor.example (email)
• www.ktk-warenkontor.example (web)
Nice to have
• Spectacular and interesting layout and design. You look at it and think, wow, that's not the normal stuff.
• We think of ourselves as bridge-builders between businesses (international producers on the one hand, and retail chains on the other hand) and we translate, organise and manage projects where both partners are involved, but it's difficult for them to cooperate due to language barriers and different working cultures.
• This is why we have the n between the B's shaped as a bridge, and the green arc supports this idea. Maybe you could play with this idea...
Should not have
• the standard layout that everybody has

```html
<!DOCTYPE html>
<html lang="de">
<head>
<meta charset="utf-8">
<title>KtK Warenkontor – Visitenkarte</title>
<link rel="stylesheet" href="https://fonts.googleapis.com/css2?family=Open+Sans:wght@400;600;700&display=swap">
<style>
  :root {
    --backdrop: #d6d6d6;
    --card-white: #ffffff;
    --brand-green: #2aaa48;
    --ink: #111111;
    --text-grey: #4a4a4a;
    --rule-grey: #8a8a8a;
  }
  * { margin: 0; padding: 0; box-sizing: border-box; }
  html, body { width: 1200px; height: 987px; overflow: hidden; }
  body {
    background: var(--backdrop);
    font-family: "Open Sans", Arial, sans-serif;
    position: relative;
  }
  .card {
    position: absolute;
    left: 293px;
    width: 615px;
    height: 350px;
    overflow: hidden;
    box-shadow: 0 4px 14px rgba(0,0,0,0.25);
  }
  .card-front { top: 130px; background: var(--card-white); }
  .card-back { top: 505px; background: var(--brand-green); }

  .wordmark {
    position: absolute;
    display: flex;
    align-items: center;
    gap: 12px;
    font-weight: 700;
    letter-spacing: 0.5px;
    line-height: 1;
  }
  .wordmark-square { width: 22px; height: 22px; flex: none; }
  .front-wordmark { left: 33px; top: 62px; color: var(--ink); font-size: 34px; }
  .front-wordmark .wordmark-square { background: var(--brand-green); }
  .back-wordmark {
    left: 0; right: 0; top: 152px; justify-content: center;
    color: var(--card-white); font-size: 42px;
  }
  .back-wordmark .wordmark-square { background: var(--card-white); width: 26px; height: 26px; }

  .edge-tab {
    position: absolute; right: -25px; top: 169px;
    width: 37px; height: 47px; border-radius: 50%;
    background: var(--brand-green);
  }
  .person { position: absolute; right: 36px; top: 160px; text-align: right; }
  .person-name { font-size: 21px; font-weight: 600; color: var(--ink); line-height: 26px; }
  .person-title { font-size: 16px; color: var(--brand-green); line-height: 24px; }
  .divider {
    position: absolute; left: 32px; right: 36px; top: 219px;
    height: 1px; background: var(--rule-grey);
  }
  .address {
    position: absolute; left: 32px; top: 254px;
    font-style: normal;
    font-size: 15px; line-height: 22px; color: var(--text-grey);
  }
  .contacts {
    position: absolute; right: 34px; top: 226px;
    list-style: none; font-size: 15px; line-height: 23.5px; color: var(--text-grey);
  }
  .contacts li { display: flex; justify-content: flex-end; align-items: center; gap: 9px; }
  .contacts svg { width: 14px; height: 14px; flex: none; fill: var(--ink); }
  .base-band { position: absolute; bottom: 0; height: 9px; }
  .base-band-dark { left: 0; width: 404px; background: var(--ink); }
  .base-band-green { left: 402px; right: 0; background: var(--brand-green); clip-path: polygon(3px 0, 100% 0, 100% 100%, 0 100%); }
  .back-web {
    position: absolute; left: 0; right: 0; top: 292px; text-align: center;
    color: var(--card-white); font-size: 15px; letter-spacing: 3px;
  }
</style>
</head>
<body>
  <section class="card card-front">
    <div class="wordmark front-wordmark"><span class="wordmark-square"></span>KtK Warenkontor</div>
    <span class="edge-tab"></span>
    <div class="person">
      <p class="person-name">Gustav Ortlieb</p>
      <p class="person-title">Geschäftsführer/ Managing Director</p>
    </div>
    <div class="divider"></div>
    <address class="address">
      KtK Warenkontor GmbH<br>Hasenbergsteige 31/2<br>70912 Lindenbach
    </address>
    <ul class="contacts">
      <li>+4971419273065
        <svg viewBox="0 0 16 16"><path d="M3.6 1.2l2.3 2.6-1.3 1.8c.9 2 2.4 3.5 4.4 4.4l1.8-1.3 2.6 2.3-1.4 2.3C7.6 13.4 2.8 8.6 1.5 2.6z"/></svg></li>
      <li>+491609381746
        <svg viewBox="0 0 16 16"><path d="M4.5 1h7v14h-7zM5.8 2.4v10h4.4v-10zM7.3 13.1h1.4v1H7.3z" fill-rule="evenodd"/></svg></li>
      <li>g.ortlieb@ktk-warenkontor.example
        <svg viewBox="0 0 16 16"><path d="M1 4h14v1.2L8 9.5 1 5.2zM1 6.6l7 4.3 7-4.3V12H1z"/></svg></li>
      <li>www.ktk-warenkontor.example
        <svg viewBox="0 0 16 16"><circle cx="8" cy="8" r="6.5" fill="none" stroke="#111" stroke-width="1.6"/><path d="M1.5 8h13M8 1.5c-3 3.5-3 9.5 0 13M8 1.5c3 3.5 3 9.5 0 13" fill="none" stroke="#111" stroke-width="1.2"/></svg></li>
    </ul>
    <div class="base-band base-band-dark"></div>
    <div class="base-band base-band-green"></div>
  </section>

  <section class="card card-back">
    <div class="wordmark back-wordmark"><span class="wordmark-square"></span>KtK Warenkontor</div>
    <p class="back-web">www.ktk-warenkontor.example</p>
  </section>
</body>
</html>
```